Header for Academic Handouts (How-to-Guides)

We are looking for a design element, which can be used as a visual header on A4-word-documents (Portrait-Set-Up). It shall be a graphic, visual language which is clearly understandable. The header height shall be between 0.75 - 1.5 inch – so it should not have too many small details. Attached below ideas/directions how the final document could look like.

The visual element shall symbolize by simple means the topic of “flipped classroom” or “active learning”. The documents with these new graphic elements will be used on handouts which are distributed in this training course:
https://www.kolvabrun.ch/en/the-kolvabrun-hochschule/education/educational-development/didaktische-weiterbildung/flipped-classroom.html

```html
<!DOCTYPE html>
<html lang="en">
<head>
<meta charset="utf-8">
<title>Flipped Classroom – Teaching Lab handout header</title>
<link rel="stylesheet" href="https://fonts.googleapis.com/css2?family=Roboto+Condensed:ital,wght@0,700;1,700&family=Open+Sans:wght@400;600&display=swap">
<style>
  :root {
    --backdrop: #e9e9e7;
    --paper: #ffffff;
    --orange: #f7960f;
    --gold: #ebc040;
    --white: #ffffff;
  }
  * { box-sizing: border-box; margin: 0; padding: 0; }
  html, body {
    width: 1200px;
    height: 1200px;
    overflow: hidden;
    background: var(--backdrop);
  }
  .page {
    position: absolute;
    left: 211px;
    top: 50px;
    width: 778px;
    height: 1100px;
    background: var(--paper);
    box-shadow: 0 6px 24px rgba(0,0,0,0.12);
  }
  .header {
    position: absolute;
    left: 0;
    top: 52px;
    width: 778px;
    height: 104px;
  }
  .header svg { position: absolute; inset: 0; }
  .header-title {
    position: absolute;
    top: 0;
    height: 104px;
    display: flex;
    align-items: center;
    font-family: "Roboto Condensed", sans-serif;
    font-weight: 700;
    color: var(--white);
    font-size: 42px;
    letter-spacing: 0.3px;
  }
  .header-title--course { left: 60px; font-style: italic; }
  .header-title--lab { left: 488px; }
  .footer-rule {
    position: absolute;
    left: 0;
    top: 960px;
    width: 778px;
    height: 4px;
    background: var(--gold);
  }
  .footer {
    position: absolute;
    left: 0;
    bottom: 0;
    width: 778px;
    height: 124px;
    background: var(--gold);
    color: var(--white);
  }
  .footer-unit {
    position: absolute;
    left: 64px;
    top: 52px;
    font-family: "Open Sans", sans-serif;
    font-weight: 600;
    font-size: 17px;
    line-height: 1.5;
  }
  .footer-brand {
    position: absolute;
    right: 60px;
    top: 30px;
    font-family: "Open Sans", sans-serif;
    font-weight: 600;
    font-size: 27px;
  }
</style>
</head>
<body>
  <div class="page">
    <header class="header">
      <svg width="778" height="104" viewBox="0 0 778 104" aria-hidden="true">
        <polygon points="20,0 462,0 422,104 20,104" fill="var(--orange)"/>
        <polygon points="474,0 778,0 778,104 434,104" fill="var(--gold)"/>
      </svg>
      <h1 class="header-title header-title--course">Flipped Classroom</h1>
      <h2 class="header-title header-title--lab">Teaching Lab</h2>
    </header>

    <div class="footer-rule"></div>
    <footer class="footer">
      <p class="footer-unit">Educational Development and Technology<br>www.let.kolvabrun.ch</p>
      <p class="footer-brand">Kolvabrun Hochschule</p>
    </footer>
  </div>
</body>
</html>
```